Stationary and Logo Design Project

We need a full corporate logo and stationary design for our company Lumvira7Q. Lumvira7Q specializes in creating custom adult sex toys using CAD and 3D Printing technologies as part of the process. The companies tagline is "made for you, by design", though this is not required to be part of the logo.

We are looking for something sensual, romantic and sexy, but not something explicit and vulgar.

As the company will be targeting mid to high-end clientele tastefulness is very important to us - this is difficult when the service we are selling is sex but can be achieved.

What we are after:

1. Logo
2. Business Card Design
3. Letterhead Design
4. Email Signature Design

File Formats we require in colour, greyscale and Black and White:

1 .AI
2 .EPS
3 .TIF
4 .PDF
5 .PNG (300 dpi)
6 .JPG (300 dpi)
7 .GIF (300 dpi)

Target Market(s)

Adults between the ages of 21 and 50 (Predominantly female but not limited to) who like there sex toys and want a custom job.

Industry/Entity Type

Adult

Requirements
Must have
• As we are planning on advertising in the future make sure the art is suitable for print advertising.
Nice to have
• The tagline "made for you, by design" on the business card, letterhead and email signature.
Should not have
• Explicit/vulgar illustrations.

"Clip-Art" should not be used.

```html
<!DOCTYPE html>
<html lang="en">
<head>
<meta charset="utf-8">
<title>Lumvira7Q Stationery</title>
<link href="https://fonts.googleapis.com/css2?family=Arimo:wght@400;700&display=swap" rel="stylesheet">
<style>
  :root {
    --bg: #e3e3e3;
    --paper: #f2f2f2;
    --ink: #151515;
    --muted: #444;
    --red: #d8202a;
    --dark: #150607;
    --dark-red: #5a0b0e;
    --rule: #bdbdbd;
  }
  * { margin: 0; padding: 0; box-sizing: border-box; }
  html, body { width: 1200px; height: 800px; overflow: hidden; }
  body {
    background: var(--bg);
    font-family: 'Arimo', Arial, sans-serif;
    color: var(--ink);
    position: relative;
  }
  .brand-name { font-weight: 700; letter-spacing: -0.5px; color: var(--ink); white-space: nowrap; }
  .brand-name.light { color: #fff; }
  .brand-dot { display: inline-block; border-radius: 50%; background: var(--red); vertical-align: middle; }
  .tagline { color: var(--ink); white-space: nowrap; }
  .tagline.light { color: #ddd; }
  .label { color: var(--red); }

  /* Letterhead */
  .letterhead {
    position: absolute; left: 160px; top: 110px; width: 370px; height: 523px;
    background: var(--paper);
  }
  .lh-brand { position: absolute; left: 30px; top: 34px; }
  .lh-brand .brand-name { font-size: 22px; }
  .lh-brand .brand-dot { width: 14px; height: 14px; margin-left: 5px; }
  .lh-brand .tagline { font-size: 8.5px; margin-top: 1px; }
  .lh-contact {
    position: absolute; left: 212px; top: 36px; padding-left: 9px;
    border-left: 1px solid var(--rule); font-size: 6.5px; line-height: 8px; white-space: nowrap;
  }
  .lh-contact .address { margin-top: 5px; }
  .lh-body { position: absolute; left: 33px; top: 128px; width: 304px; font-size: 6px; line-height: 10.5px; text-align: justify; }
  .lh-body p { margin-bottom: 9px; }
  .lh-signoff { position: absolute; left: 33px; top: 406px; font-size: 6px; }
  .signature { position: absolute; left: 33px; top: 418px; width: 110px; height: 22px; }
  .signer { position: absolute; left: 92px; top: 445px; font-size: 6px; line-height: 8px; }
  .lh-band { position: absolute; left: 0; bottom: 0; width: 100%; height: 11px; display: flex; }
  .lh-band .red { width: 39%; background: var(--red); }
  .lh-band .black { flex: 1; background: var(--ink); }

  /* Business cards */
  .card { position: absolute; width: 165px; height: 92px; }
  .card-front {
    left: 595px; top: 240px;
    background: radial-gradient(ellipse at 75% 40%, var(--dark-red), var(--dark) 70%);
  }
  .card-front .brand { position: absolute; left: 14px; top: 32px; }
  .card-front .brand-name { font-size: 15px; }
  .card-front .brand-dot { width: 9px; height: 9px; margin-left: 4px; }
  .card-front .tagline { font-size: 5.5px; }
  .card-front .url { position: absolute; left: 14px; top: 70px; font-size: 5px; color: var(--red); letter-spacing: 0.5px; }

  .card-back { left: 790px; top: 240px; background: #f4f4f4; }
  .card-back .side-bar { position: absolute; right: 0; top: 0; width: 5px; height: 100%; background: var(--ink); }
  .card-back .side-bar::before { content: ""; position: absolute; top: 0; left: 0; width: 100%; height: 38%; background: var(--red); }
  .card-back .brand { position: absolute; left: 13px; top: 30px; }
  .card-back .brand-name { font-size: 12px; }
  .card-back .brand-dot { width: 7px; height: 7px; margin-left: 3px; }
  .card-back .tagline { font-size: 4.5px; }
  .card-back .person { position: absolute; right: 13px; top: 31px; text-align: right; }
  .card-back .person .name { font-size: 6px; font-weight: 700; color: var(--red); white-space: nowrap; }
  .card-back .person .role { font-size: 4.5px; }
  .card-back .details { position: absolute; right: 13px; top: 52px; text-align: right; font-size: 4px; line-height: 5.5px; white-space: nowrap; }
  .card-back .address { position: absolute; right: 13px; top: 75px; font-size: 4.2px; white-space: nowrap; }

  /* Email signature */
  .email-signature {
    position: absolute; left: 585px; top: 417px; width: 440px; height: 137px;
    background: radial-gradient(ellipse at 72% 100%, #6a0b10, var(--dark) 60%);
    color: #eee;
  }
  .email-signature .brand { position: absolute; left: 27px; top: 38px; }
  .email-signature .brand-name { font-size: 27px; }
  .email-signature .brand-dot { width: 16px; height: 16px; margin-left: 6px; }
  .email-signature .tagline { font-size: 10px; }
  .email-signature .url { position: absolute; left: 28px; top: 96px; font-size: 8px; color: var(--red); letter-spacing: 1px; }
  .email-signature .person { position: absolute; left: 255px; top: 32px; }
  .email-signature .name { font-size: 11px; font-weight: 700; color: var(--red); }
  .email-signature .role { font-size: 8px; }
  .email-signature .details { position: absolute; left: 255px; top: 63px; font-size: 7.5px; line-height: 9.5px; white-space: nowrap; }
  .email-signature .address { position: absolute; left: 255px; top: 95px; font-size: 7.5px; white-space: nowrap; }
</style>
</head>
<body>

<section class="letterhead">
  <div class="lh-brand">
    <div><span class="brand-name">Lumvira7Q</span><span class="brand-dot"></span></div>
    <div class="tagline">made for you, by design</div>
  </div>
  <div class="lh-contact">
    <div><span class="label">p:</span> (555) 201-4476</div>
    <div><span class="label">e:</span> mholloway@lumvira7q.com</div>
    <div><span class="label">w:</span> www.lumvira7q.com</div>
    <div class="address">1480 Corvel Ave., Linden Falls, LA 70412</div>
  </div>
  <div class="lh-body">
    <p>Dear Client,</p>
    <p>Lorem ipsum dolor sit amet, consectetur adipisicing elit, sed do eiusmod tempor incididunt ut labore et dolore magna aliqua. Ut enim ad minim veniam, quis nostrud exercitation ullamco laboris nisi ut aliquip ex ea commodo consequat. Duis aute irure dolor in reprehenderit in voluptate velit esse cillum dolore eu fugiat nulla pariatur. Excepteur sint occaecat cupidatat non proident, sunt in culpa qui officia deserunt mollit anim id est laborum.</p>
    <p>Lorem ipsum dolor sit amet, consectetur adipisicing elit, sed do eiusmod tempor incididunt ut labore et dolore magna aliqua. Ut enim ad minim veniam, quis nostrud exercitation ullamco laboris nisi ut aliquip ex ea commodo consequat. Duis aute irure dolor in reprehenderit in voluptate velit esse cillum dolore eu fugiat nulla pariatur. Excepteur sint occaecat cupidatat non proident, sunt in culpa qui officia deserunt mollit anim id est laborum.</p>
    <p>Lorem ipsum dolor sit amet, consectetur adipisicing elit, sed do eiusmod tempor incididunt ut labore et dolore magna aliqua. Ut enim ad minim veniam, quis nostrud exercitation ullamco laboris nisi ut aliquip ex ea commodo consequat. Duis aute irure dolor in reprehenderit in voluptate velit esse cillum dolore eu fugiat nulla pariatur. Excepteur sint occaecat cupidatat non proident, sunt in culpa qui officia deserunt mollit anim id est laborum.</p>
    <p>Lorem ipsum dolor sit amet, consectetur adipisicing elit, sed do eiusmod tempor incididunt ut labore et dolore magna aliqua. Ut enim ad minim veniam, quis nostrud exercitation ullamco laboris nisi ut aliquip ex ea commodo consequat. Duis aute irure dolor in reprehenderit in voluptate velit esse cillum dolore eu fugiat nulla pariatur. Excepteur sint occaecat cupidatat non proident, sunt in culpa qui officia deserunt mollit anim id est laborum.</p>
  </div>
  <div class="lh-signoff">Yours Sincerely,</div>
  <svg class="signature" viewBox="0 0 110 22" role="img" aria-label="Handwritten signature of Elias Brandt">
    <rect x="0" y="4" width="110" height="14" fill="#dcdcdc"/>
  </svg>
  <div class="signer">Elias Brandt<br>Executive manager</div>
  <div class="lh-band"><span class="red"></span><span class="black"></span></div>
</section>

<section class="card card-front">
  <div class="brand">
    <div><span class="brand-name light">Lumvira7Q</span><span class="brand-dot"></span></div>
    <div class="tagline light">made for you, by design</div>
  </div>
  <div class="url">www.lumvira7q.com</div>
</section>

<section class="card card-back">
  <div class="brand">
    <div><span class="brand-name">Lumvira7Q</span><span class="brand-dot"></span></div>
    <div class="tagline">made for you, by design</div>
  </div>
  <div class="person">
    <div class="name">Maren Holloway</div>
    <div class="role">Manager</div>
  </div>
  <div class="details">
    <div>(555) 201-4476 <span class="label">p</span></div>
    <div>mholloway@lumvira7q.com <span class="label">e</span></div>
    <div>www.lumvira7q.com <span class="label">w</span></div>
  </div>
  <div class="address">1480 Corvel Ave., Linden Falls, LA 70412</div>
  <span class="side-bar"></span>
</section>

<section class="email-signature">
  <div class="brand">
    <div><span class="brand-name light">Lumvira7Q</span><span class="brand-dot"></span></div>
    <div class="tagline light">made for you, by design</div>
  </div>
  <div class="url">www.Lumvira7Q.com</div>
  <div class="person">
    <div class="name">Maren Holloway</div>
    <div class="role">Manager</div>
  </div>
  <div class="details">
    <div><span class="label">p:</span> (555) 201-4476</div>
    <div><span class="label">e:</span> mholloway@lumvira7q.com</div>
    <div><span class="label">w:</span> www.lumvira7q.com</div>
  </div>
  <div class="address">1480 Corvel Ave., Linden Falls, LA 70412</div>
</section>

</body>
</html>
```